Upmarket designer fashion & gift boutique card design

I need a business card that captures the vision of my customer & store. I am a ladies fashion boutique in the beautiful Northern Beaches of Sydney. I stock top australian designer fashion that is bold, colourful, & eccentric. My store also carries quirky & retro gift ware & unique statement jewellery. I want a card that is as colourful & eccentric as the designers I stock & the customer I attract. I love bold bright colours, leopard print, abstract or geometric shapes but nothing to fluffy or girly. I have attached my logo which is to be included on one side of the card.

Target Market(s)

25+ with a strong focus on the fabulous 30's & 40's

Industry/Entity Type

Boutique

Contact Information for Business Card

Delia Marchant, Director, Shop 5/17 Kellering Crescent Tarrowin Bay NSW 2186, delia@tullaverra.com.au ABN 71 308 916 254, mobile number 0438 762 104 www.facebook.com/tullaverra

Font styles to use
Sans Serif

Colors

Designer to choose colors to be used in the design.

Requirements
Must have
• Open mind- although leopard or zebra print would win some votes
Nice to have
• Unique, fun,bold, quirky & different - hit me with your best shot!
Should not have
• No swirly/running writing text please

```html
<!DOCTYPE html>
<html lang="en">
<head>
<meta charset="utf-8">
<title>tullaverra – business card</title>
<link rel="stylesheet" href="https://fonts.googleapis.com/css2?family=Arimo:wght@400;700&display=swap">
<style>
  :root {
    --paper: #ffffff;
    --ink: #111111;
    --muted: #4d4d4d;
    --brand-teal: #2ab3d6;
    --name-sky: #3fc2ee;
    --title-blue: #1a30c6;
    --rule-violet: #8a2be2;
  }
  * { margin: 0; padding: 0; box-sizing: border-box; }
  html, body {
    width: 987px; height: 1200px; overflow: hidden;
    background: var(--paper);
    font-family: "Arimo", Arial, sans-serif;
  }
  .canvas { position: relative; width: 987px; height: 1200px; }

  /* Front: logo side */
  .front { position: absolute; left: 0; top: 0; width: 987px; height: 621px; background: var(--paper); }
  .front-brand {
    position: absolute; left: 86px; top: 205px; width: 858px;
    font-weight: 700; font-size: 168px; line-height: 1;
    letter-spacing: -4px; color: var(--brand-teal); text-align: center;
  }
  .front-tagline {
    position: absolute; right: 48px; top: 404px;
    font-weight: 400; font-size: 36px; color: var(--ink); letter-spacing: 1px;
  }

  /* Back: contact side */
  .back {
    position: absolute; left: 0; top: 621px; width: 987px; height: 579px;
    border-top: 1px solid var(--rule-violet); overflow: hidden;
  }
  .back-pattern {
    position: absolute; inset: 0;
    background:
      linear-gradient(90deg, rgba(255,255,255,0.95) 0%, rgba(255,255,255,0.75) 35%, rgba(255,255,255,0) 62%),
      linear-gradient(160deg, #f7f2ff 0%, #ffe86a 40%, #ff6fd0 58%, #c540e8 75%, #6ad4ff 100%);
  }
  .back-brand {
    position: absolute; left: 88px; top: 28px;
    font-weight: 700; font-size: 78px; line-height: 1;
    letter-spacing: -3px; color: var(--ink);
  }
  .contact { position: absolute; left: 91px; top: 196px; }
  .contact-name { font-size: 40px; color: var(--name-sky); line-height: 1.15; }
  .contact-role { font-size: 40px; color: var(--title-blue); line-height: 1.1; }
  .contact-line { font-size: 31px; color: var(--ink); line-height: 1; margin-top: 18px; }
  .contact-line:first-of-type { margin-top: 24px; }
  .contact-line strong { font-weight: 700; letter-spacing: -1px; }
  .address { position: absolute; left: 91px; top: 410px; font-size: 27px; line-height: 37px; color: var(--muted); }
</style>
</head>
<body>
<main class="canvas">
  <section class="front">
    <div class="front-brand">tullaverra</div>
    <div class="front-tagline">Gift and Fashion</div>
  </section>

  <section class="back">
    <div class="back-pattern" role="img" aria-label="Bright multicoloured leopard print with geometric triangles, fading to white on the left"></div>
    <div class="back-brand">tullaverra</div>
    <div class="contact">
      <div class="contact-name">delia marchant</div>
      <div class="contact-role">director</div>
      <p class="contact-line"><strong>mobile</strong> 0438 762 104</p>
      <p class="contact-line"><strong>email</strong> delia@tullaverra.com.au</p>
    </div>
    <div class="address">
      Shop 5/17 Kellering Crescent<br>
      Tarrowin Bay NSW 2186<br>
      ABN 71 308 916 254<br>
      www.facebook.com/tullaverra
    </div>
  </section>
</main>
</body>
</html>
```